Speaker and Author Website

I need a website to promote myself as a public speaker and a site where I can promote my books. I would like to have a website similar to this page

http://tobiasvarnell.com/

The categories I would be covering on my site are the following:

Motivation, Leadership, Technology, Small Business, Inspiration

I want a wordpress site, so it is easy for me to make changes when needed. I need a blog site within my site to.

```html
<!DOCTYPE html>
<html lang="en">
<head>
<meta charset="utf-8">
<title>Mara Quintell — Speaker &amp; Author</title>
<link href="https://fonts.googleapis.com/css2?family=Arimo:ital,wght@0,400;0,700;1,400&display=swap" rel="stylesheet">
<style>
:root{
  --navy:#14143a;
  --panel:#f5f5f5;
  --bar:#6d6d6d;
  --bar-line:#8a8a8a;
  --head-gray:#6b6b6b;
  --text:#777;
  --dark:#222;
  --foot:#444;
  --foot-line:#5c5c5c;
  --foot-box:#333;
  --light:#eee;
  --tag:#cfcfcf;
}
*{margin:0;padding:0;box-sizing:border-box}
html,body{width:1130px;height:1200px;overflow:hidden}
body{position:relative;background:#fff;font-family:"Arimo",Arial,sans-serif;color:var(--text)}
.abs{position:absolute}
a{color:inherit;text-decoration:none}

.topbar{left:0;top:0;width:1130px;height:50px;background:var(--navy)}
.topnav{left:330px;top:15px;display:flex;font-size:14px;color:#ddd}
.topnav a{padding:0 11px;border-left:1px solid #666;line-height:20px}
.topnav a:first-child{border-left:none}
.search{left:803px;top:11px;width:234px;height:28px;background:#fff;border-radius:3px}
.search svg{position:absolute;right:6px;top:3px}

.hero{left:97px;top:75px;width:935px;height:202px;background:var(--panel)}
.portrait{left:118px;top:16px;width:198px;height:212px;border:3px solid #fff;border-radius:6px;box-shadow:0 1px 5px rgba(0,0,0,.4);background:linear-gradient(160deg,#c92020,#9e1616 55%,#e8756e)}
.brand{left:128px;top:242px;font-size:24px;font-weight:700;letter-spacing:1px;color:#555}
.brand b{color:var(--navy)}
.tagline{left:330px;top:130px;width:700px;text-align:center;font-size:23px;font-weight:700;line-height:30px;color:var(--tag);letter-spacing:.3px}

.catbar{left:97px;top:277px;width:935px;height:48px;background:var(--bar);display:flex}
.catbar a{height:48px;line-height:48px;text-align:center;font-size:21px;font-weight:700;color:#e6e6e6;border-left:1px solid var(--bar-line)}
.catbar a:first-child{border-left:none}
.catbar a.active{color:var(--navy)}

.post-title{left:108px;top:364px;font-size:20px;font-weight:700;color:var(--dark)}
.title-rule{left:97px;top:389px;width:547px;height:4px;background:#ccc}
.share{left:109px;top:404px;display:flex;align-items:center;gap:6px;font-size:11px}
.btn{height:20px;line-height:20px;padding:0 7px;border-radius:3px;color:#fff;font-weight:700;background:var(--head-gray)}
.count{height:20px;line-height:18px;padding:0 5px;border:1px solid #ccc;border-radius:3px;color:#777;margin-right:10px}
.spread{display:flex;align-items:center;gap:5px;color:#777}
.spread i{width:18px;height:18px;background:var(--head-gray);border-radius:3px;display:block}

.feature{left:102px;top:436px;width:539px;height:351px;border:1px solid #ddd;background:linear-gradient(180deg,#3a3b8a 0%,#5a2a38 35%,#a31a1e 60%,#2a1414 100%)}
.excerpt{left:102px;top:803px;width:545px;font-size:12.5px;line-height:16px;color:#888}
.meta{left:101px;top:878px;font-size:10.5px;color:#888;display:flex;gap:22px}
.meta a{color:#222;text-decoration:underline}
.readmore{font-size:13.5px;color:#222;text-decoration:underline}

.side-head{left:687px;width:345px;height:33px;line-height:33px;padding-left:8px;background:var(--head-gray);color:#fff;font-size:19px;font-weight:700}
.book{left:687px;top:396px;width:102px;height:153px;background:linear-gradient(180deg,#d4262a,#b81b20 60%,#6f1214)}
.bio{left:794px;top:395px;width:242px;font-size:11.3px;line-height:15.6px;color:#888}
.rule{left:687px;width:345px;height:2px;background:#999}
.item{left:690px;width:345px}
.thumb{position:absolute;left:0;top:0;width:62px;height:62px;border:1px solid #ddd;padding:3px}
.thumb span{display:block;width:100%;height:100%;background:linear-gradient(135deg,#c83030,#7a1a1a 60%,#3a2020)}
.item h4{position:absolute;left:71px;top:0;font-size:13.5px;color:var(--dark)}
.item p{position:absolute;left:71px;top:18px;width:280px;font-size:11px;line-height:16px;color:#999}
.item .readmore{position:absolute;left:247px;top:52px}

footer{color:var(--light)}
.footer{left:0;top:936px;width:1130px;height:264px;background:var(--foot)}
.contact{left:105px;display:flex;align-items:center;gap:10px;font-size:14px;color:var(--light)}
.ico{width:32px;height:32px;background:#2e2e2e;border-radius:3px;display:flex;align-items:center;justify-content:center}
.contact a{text-decoration:underline}
.fhead{font-size:12px;font-weight:700;color:#fff;top:968px}
.fline{height:1px;background:var(--foot-line);top:994px}
.catlist{left:333px;top:1012px;width:205px;list-style:none;font-size:14px;color:var(--light)}
.catlist li{height:29px;line-height:28px;border-bottom:1px solid var(--foot-line);padding-left:10px;position:relative}
.catlist li::before{content:"›";position:absolute;left:0;font-size:12px}
.quote{left:577px;top:1010px;width:205px;height:107px;background:var(--foot-box);padding:10px 12px;font-size:12.5px;font-style:italic;line-height:16px;color:#ddd}
.quote-by{left:577px;top:1140px;width:205px;text-align:right;font-size:13px;font-weight:700;color:#fff}
.more-link{left:577px;top:1157px;font-size:14px;color:var(--light)}
.about{left:820px;top:1010px;width:210px;font-size:12px;line-height:18px;color:#fff}
</style>
</head>
<body>

<div class="abs topbar"></div>
<nav class="abs topnav">
  <a href="#">Home</a><a href="#">About</a><a href="#">Speaking</a><a href="#">Recommended Books</a><a href="#">Contact</a>
</nav>
<div class="abs search">
  <svg width="24" height="22" viewBox="0 0 24 22"><circle cx="9" cy="9" r="7" fill="none" stroke="#ccc" stroke-width="3"/><line x1="14" y1="14" x2="21" y2="20" stroke="#ccc" stroke-width="4" stroke-linecap="round"/></svg>
</div>

<header>
  <div class="abs hero"></div>
  <div class="abs portrait" role="img" aria-label="Portrait of the speaker holding a microphone on stage"></div>
  <div class="abs brand">MARA <b>QUINTELL</b></div>
  <p class="abs tagline">Award Winning Technology Consultant, Entrepreneur,<br>Small Business Leader, and Motivational Speaker</p>
</header>

<nav class="abs catbar">
  <a href="#" class="active" style="width:174px">Technology</a>
  <a href="#" style="width:162px">Leadership</a>
  <a href="#" style="width:153px">Motivation</a>
  <a href="#" style="width:212px">Small Business</a>
  <a href="#" style="width:234px">Entrepreneurship</a>
</nav>

<main>
  <h2 class="abs post-title">Lorem Ipsum is simply dummy text</h2>
  <div class="abs title-rule"></div>
  <div class="abs share">
    <span class="btn">Share</span><span class="count">472</span>
    <span class="btn">Post</span><span class="count">17</span>
    <span class="btn">Plus</span><span class="count">4</span>
    <span class="btn">Save</span><span class="count">9</span>
    <span class="spread"><i></i>SpreadIt</span>
  </div>
  <div class="abs feature" role="img" aria-label="Conference hall with audience facing a lit stage and two projection screens"></div>
  <p class="abs excerpt">Lorem Ipsum is simply dummy text of the printing and typesetting industry. Lorem Ipsum has been the industry's standard dummy text ever since the 1500s, when an unknown printer took a galley of type and scrambled it to make a type specimen book. It has survived not only five centuries, but also the leap into electronic typesetting, remaining essentially unchanged...</p>
  <div class="abs meta">
    <span>Posted In <a href="#">Technology</a></span>
    <span>Posted by <a href="#">admin</a></span>
    <span>Post type <b style="color:#222;font-weight:400">Image</b></span>
  </div>
  <a href="#" class="abs readmore" style="left:555px;top:875px">Read More →</a>
</main>

<aside>
  <h3 class="abs side-head" style="top:357px">Authour</h3>
  <div class="abs book" role="img" aria-label="Cover of the book Grounded Growth Guide"></div>
  <p class="abs bio">Best-Selling Author, Mara Quintell and her company NetBridge Partners, Inc., is considered one of the top Information Technology service and solutions provider in the country. Mara Quintell was inducted into the Guild of Acclaimed Authors and was presented with a Quill Honor in September 2013 for her contribution to the Best-Selling Book "Grounded Growth Guide." ...</p>
  <a href="#" class="abs readmore" style="left:937px;top:537px">Read More →</a>
  <div class="abs rule" style="top:561px"></div>

  <h3 class="abs side-head" style="top:575px">Latest Post</h3>

  <div class="abs item" style="top:616px">
    <div class="thumb" role="img" aria-label="Author holding her book"><span></span></div>
    <h4>Lorem Ipsum is simply</h4>
    <p>Lorem Ipsum is simplyLorem Ipsum is simply Lorem Ipsum is simply Lorem Ipsum is simply ...</p>
    <a href="#" class="readmore">Read More →</a>
  </div>
  <div class="abs rule" style="top:692px;left:690px;width:342px;height:1px"></div>
  <div class="abs item" style="top:702px">
    <div class="thumb" role="img" aria-label="Author holding her book"><span></span></div>
    <h4>Lorem Ipsum is simply</h4>
    <p>Lorem Ipsum is simplyLorem Ipsum is simply Lorem Ipsum is simply Lorem Ipsum is simply ...</p>
    <a href="#" class="readmore">Read More →</a>
  </div>
  <div class="abs rule" style="top:778px;left:690px;width:342px;height:1px"></div>
  <div class="abs item" style="top:788px">
    <div class="thumb" role="img" aria-label="Author holding her book"><span></span></div>
    <h4>Lorem Ipsum is simply</h4>
    <p>Lorem Ipsum is simplyLorem Ipsum is simply Lorem Ipsum is simply Lorem Ipsum is simply ...</p>
    <a href="#" class="readmore">Read More →</a>
  </div>
  <div class="abs rule" style="top:864px;left:690px;width:342px;height:1px"></div>
  <div class="abs item" style="top:874px">
    <div class="thumb" role="img" aria-label="Author holding her book"><span></span></div>
    <h4>Lorem Ipsum is simply</h4>
    <p>Lorem Ipsum is simplyLorem Ipsum is simply Lorem Ipsum is simply Lorem Ipsum is simply ...</p>
  </div>
</aside>

<footer>
  <div class="abs footer"></div>

  <div class="abs contact" style="top:976px">
    <span class="ico"><svg width="18" height="18" viewBox="0 0 18 18"><path d="M4 1l3 4-2 2c1 2 3 4 5 5l2-2 4 3-2 3C8 16 2 10 1 4z" fill="#eee"/></svg></span>
    <span>0800 555 214</span>
  </div>
  <div class="abs contact" style="top:1017px">
    <span class="ico"><svg width="14" height="14"><rect width="14" height="14" rx="2" fill="#eee"/></svg></span>
    <a href="#">circlesay</a>
  </div>
  <div class="abs contact" style="top:1058px">
    <span class="ico"><svg width="14" height="14"><circle cx="7" cy="7" r="6" fill="#eee"/></svg></span>
    <a href="#">chirpline</a>
  </div>
  <div class="abs contact" style="top:1099px">
    <span class="ico"><svg width="18" height="13" viewBox="0 0 18 13"><rect x="1" y="1" width="16" height="11" fill="none" stroke="#eee" stroke-width="1.5"/><path d="M1 1l8 6 8-6" fill="none" stroke="#eee" stroke-width="1.5"/></svg></span>
    <a href="#">Send us a Message</a>
  </div>

  <h5 class="abs fhead" style="left:333px">CATEGORY</h5>
  <div class="abs fline" style="left:333px;width:205px"></div>
  <ul class="abs catlist">
    <li>Technology</li><li>Leadership</li><li>Motivation</li><li>Small Business</li><li>Entrepreneurship</li>
  </ul>

  <h5 class="abs fhead" style="left:577px">TESTIMONIALS</h5>
  <div class="abs fline" style="left:577px;width:205px"></div>
  <blockquote class="abs quote">Lorem Ipsum is simply dummy text of the printing and type setting industry Lorem Ipsum has been the industry's standard dummy text ever since the 1500s ...</blockquote>
  <div class="abs quote-by">Lorem Ipsum</div>
  <a href="#" class="abs more-link">View more testimonials</a>

  <h5 class="abs fhead" style="left:820px">ABOUT US</h5>
  <div class="abs fline" style="left:820px;width:205px"></div>
  <p class="abs about">Best-Selling Author, Mara Quintell and her company NetBridge Partners, Inc., is considered one of the top Information Technology service and solutions provider in the country. "</p>
</footer>

</body>
</html>
```